Talvoro Equity LLC

Need Professional Business cards for New Investment Fund

Target Market(s)

High Quality investors

Industry/Entity Type

Financial

Contact Information for Business Card

Phone Number +1 555 284 6190
Name Milan Dorovsky
Title Fund Manager
email md@FundTalvoro.com
Website www.FundTalvoro.com

Colors

Designer to choose colors to be used in the design.

Requirements
Must have
• Must have our Logo and all of the above. Must be made so lettering and loge can be raised

```html
<!DOCTYPE html>
<html lang="en">
<head>
<meta charset="utf-8">
<title>Talvoro Equity LLC – Business Cards</title>
<link rel="stylesheet" href="https://fonts.googleapis.com/css2?family=Montserrat:wght@400;500&display=swap">
<style>
  :root {
    --backdrop: #5d9850;
    --card-top: #282828;
    --card-bottom: #0c0c0c;
    --accent: #5dbb4c;
    --muted: #5a6a57;
  }
  * { box-sizing: border-box; margin: 0; padding: 0; }
  html, body {
    width: 1200px;
    height: 1096px;
    overflow: hidden;
    background: var(--backdrop);
    font-family: "Montserrat", Arial, sans-serif;
  }
  .card {
    position: absolute;
    width: 550px;
    height: 356px;
    background: linear-gradient(170deg, var(--card-top) 0%, #1a1a1a 55%, var(--card-bottom) 100%);
    color: var(--accent);
  }
  .card--front { left: 442px; top: 145px; }
  .card--back  { left: 148px; top: 548px; }

  .front-frame {
    position: absolute;
    left: 39px;
    top: 39px;
    width: 472px;
    height: 279px;
    border: 2px solid var(--accent);
  }
  .brand {
    position: absolute;
    left: 0;
    right: 0;
    top: 150px;
    display: flex;
    align-items: center;
    justify-content: center;
    gap: 12px;
  }
  .brand-square {
    width: 22px;
    height: 22px;
    background: var(--accent);
  }
  .brand-name {
    font-size: 26px;
    font-weight: 500;
    letter-spacing: 0.12em;
    text-transform: uppercase;
    color: var(--accent);
  }

  .holder-name {
    position: absolute;
    left: 23px;
    top: 19px;
    font-size: 28px;
    font-weight: 500;
    letter-spacing: 0.005em;
  }
  .holder-title {
    position: absolute;
    left: 23px;
    top: 55px;
    font-size: 14px;
    font-weight: 400;
  }
  .contact-phone {
    position: absolute;
    left: 22px;
    bottom: 26px;
    writing-mode: vertical-rl;
    transform: rotate(180deg);
    font-size: 19px;
    font-weight: 400;
    letter-spacing: 0.02em;
  }
  .contact-email {
    position: absolute;
    right: 24px;
    top: 25px;
    writing-mode: vertical-rl;
    font-size: 19px;
    font-weight: 400;
    letter-spacing: 0.02em;
  }
  .contact-web {
    position: absolute;
    right: 25px;
    bottom: 22px;
    font-size: 19px;
    font-weight: 400;
    letter-spacing: 0.02em;
  }
</style>
</head>
<body>
  <section class="card card--front" aria-label="Card front">
    <div class="front-frame"></div>
    <div class="brand">
      <span class="brand-square"></span>
      <span class="brand-name">Talvoro Equity</span>
    </div>
  </section>

  <section class="card card--back" aria-label="Card back">
    <h1 class="holder-name">Milan Dorovsky</h1>
    <p class="holder-title">Title Fund Manager</p>
    <p class="contact-phone">+1 555 284 6190</p>
    <p class="contact-email">md@FundTalvoro.com</p>
    <p class="contact-web">www.FundTalvoro.com</p>
  </section>
</body>
</html>
```